Broschüre für Sicherheitsdienstleistungen
Zielgruppe
Sicherheitsunternehmen
Hallo,
Wir möchten gerne eine Broschüre (ca. 12 Seiten) gestalten lassen wo alle unsere verschiedene Dienstleistungen Beschrieben werden und unser unternehmen vorgestellt wird an den Kunden.
Als Hard copy Version von unsere neue Seite : http://kwt.seitenplanung-beispiel.de
Das Design soll Freundlich und Modern Gestaltet werden.
Farbtöne gerne in Weiss und Dunkel Blau
Produktdetails :
Rückendrahtheftung links, 4/4-farbig (beidseitiger Druck, CMYK)
ab 250 g wird der Umschlag zusätzlich genutet
Veredelung Umschlag
beidseitiger UV-Lack glänzend
Format
DIN A4 (21 x 29,7 cm)
Details: Hochformat
Seitenanzahl ca. 10 - 12 (Excl. Umschlag)
Material Umschlag
250g Bilderdruck glänzend
New Website Design :
http://kwt.seitenplanung-beispiel.de

```html
<!DOCTYPE html>
<html lang="de">
<head>
<meta charset="utf-8">
<title>Broschüre – Empfangsdienst und Sicherheit im Einzelhandel</title>
<link href="https://fonts.googleapis.com/css2?family=Fira+Sans:wght@300;400;600;700&family=Fira+Sans+Condensed:wght@300;400;500;600;700&family=Arimo:wght@400;700&display=swap" rel="stylesheet">
<style>
  :root{
    --navy:#3a5272;
    --navy-deep:#2f4563;
    --panel:rgba(70,95,130,.86);
    --ink:#1d1d1f;
    --accent-text:#3f5f86;
    --white:#ffffff;
    --box:#e4e6ec;
  }
  *{margin:0;padding:0;box-sizing:border-box}
  html,body{width:1200px;height:848px;overflow:hidden;background:#fff}
  .spread{position:relative;width:1200px;height:848px;overflow:hidden;font-family:"Fira Sans",sans-serif}

  /* left page */
  .page-left{position:absolute;left:0;top:0;width:600px;height:848px;overflow:hidden}
  .photo-office{position:absolute;inset:0;background:linear-gradient(110deg,#6f7a5a 0%,#8a8f86 25%,#b8a99a 50%,#b73a45 72%,#6c3a3a 85%,#c9b79f 100%)}
  .panel{position:absolute;left:37px;top:37px;width:527px;height:759px;background:var(--panel)}
  .page-no{position:absolute;top:0;width:30px;height:37px;background:var(--navy);color:#fff;font:600 17px/37px "Fira Sans Condensed",sans-serif;text-align:center}
  .page-left .page-no{left:37px}
  .tag-light{position:absolute;left:58px;top:71px;padding:0 10px;height:19px;background:#fff;color:var(--navy);font:500 14px/19px "Fira Sans Condensed",sans-serif}
  .title-left{position:absolute;left:58px;top:104px;color:#fff;font-family:"Fira Sans Condensed",sans-serif;font-size:29px;line-height:35px;font-weight:400}
  .title-left b{font-weight:700;border-bottom:1px solid #fff}
  .intro-left{position:absolute;left:58px;top:202px;width:476px;color:#fff;font:300 10.5px/16px "Fira Sans Condensed",sans-serif;text-align:justify;hyphens:auto}
  .block{position:absolute;left:58px;width:476px;color:#fff;font:400 8.6px/10.9px "Fira Sans Condensed",sans-serif;text-align:justify;hyphens:auto}
  .block h3{display:inline-block;background:#fff;color:var(--navy);font:600 8.6px/11.5px "Fira Sans Condensed",sans-serif;padding:0 2px;margin-bottom:11px}
  .reasons{position:absolute;left:49px;top:631px;width:501px;height:158px;background:var(--box);padding:24px 9px;color:var(--ink)}
  .reasons h4{font:700 10.3px/12px Arimo,sans-serif;font-variant:small-caps;margin-bottom:9px;letter-spacing:.1px}
  .reasons ul{list-style:none}
  .reasons li{position:relative;padding-left:18px;font:400 9.2px/12px "Fira Sans",sans-serif;margin-bottom:8.5px}
  .reasons li svg{position:absolute;left:0;top:2px}

  /* right page */
  .page-right{position:absolute;left:600px;top:0;width:600px;height:848px;background:#fff}
  .photo-shop{position:absolute;left:0;top:0;width:600px;height:254px;background:linear-gradient(100deg,#5c6a74 0%,#a79a8e 30%,#2f4f5c 55%,#b07a55 72%,#2e7f7a 100%)}
  .page-right .page-no{left:533px}
  .tag-dark{position:absolute;left:36px;top:235px;width:88px;height:19px;background:var(--navy-deep);color:#fff;font:500 14px/19px "Fira Sans Condensed",sans-serif;text-align:center}
  .title-right{position:absolute;left:36px;top:268px;font-family:"Fira Sans Condensed",sans-serif;font-weight:300;font-size:28px;line-height:32px;color:var(--ink);letter-spacing:.5px}
  .title-right b{color:var(--navy);font-weight:600;border-bottom:1.5px solid var(--navy);margin-left:10px}
  .intro-right{position:absolute;left:36px;top:316px;width:528px;color:var(--accent-text);font:400 10.2px/16.1px "Fira Sans",sans-serif;text-align:justify}
  .col{position:absolute;top:408px;color:var(--ink);font:400 8.5px/10.9px Arimo,sans-serif;text-align:justify;hyphens:auto;letter-spacing:-.1px}
  .col .sub{background:var(--navy);color:#fff;font-weight:700;box-decoration-break:clone;-webkit-box-decoration-break:clone}
  .col p{margin-bottom:11px}
  .c1{left:36px;width:174px}
  .c2{left:224px;width:163px}
  .c3{left:400px;width:164px}
</style>
</head>
<body>
<div class="spread">

  <section class="page-left">
    <div class="photo-office" role="img" aria-label="Foto: Empfangsmitarbeiterin im Büro an einem Laptop"></div>
    <div class="panel"></div>
    <div class="page-no">12</div>
    <div class="tag-light">KWT SECURA</div>
    <h1 class="title-left"><b>EMPFANGSDIENST</b><br>UND <b>HOSTESSENSERVICE</b></h1>
    <p class="intro-left">Bei der KWT SECURA GmbH wird Servicequalität großgeschrieben. Sie erhalten von uns nicht nur umfassende Dienstleistungen im Bereich Sicherheit, sondern auch viele weitere hochwertige Zusatzleistungen. Darunter nicht zuletzt: Unseren professionellen Hostessenservice und Empfangsdienst.</p>

    <div class="block" style="top:259px">
      <h3>Erfolg mit der KWT SECURA GmbH</h3>
      <p>Der Empfangsdienst und Hostessenservice der KWT SECURA GmbH kommt bei Ihren Gästen mit Sicherheit gut an. Schließlich wissen wir: Nur zuvorkommendes und gut ausgebildetes Empfangspersonal präsentiert Ihr Unternehmen und Ihre Marke optimal. Denn der Empfangsdienst und die Hostessen sind oft der erste Kontakt, den Besucher und potenzielle Geschäftskunden zu Ihrem Unternehmen haben. Genau aus diesem Grund weiß unser Team genau, wie man einen professionellen und souveränen Eindruck hinterlässt. Bei uns buchen Sie ausgewählte Damen und Herren mit exzellenten Umgangsformen.</p>
    </div>

    <div class="block" style="top:357px">
      <h3>Flexible und qualifizierte Mitarbeiter</h3>
      <p>Unser Empfangsdienst leistet noch wesentlich mehr, als mit Kompetenz und einem guten Auftritt zu überzeugen. Neben der höflichen Begrüßung von Gästen bedienen unsere Mitarbeiter im Empfangs- oder Pförtendienst zudem die Telefonanlage, führen Eingangskontrollen durch oder nehmen Anlieferungen entgegen. Die Möglichkeiten sind fast unbegrenzt: Im Bereich Personal und Organisation kann die KWT SECURA GmbH auf einen großen Mitarbeiterstamm an speziell ausgebildeten Fachkräften zugreifen. Sprechen Sie uns an, wir stellen garantiert das passende Team für Sie zusammen und stehen Ihnen gerne als langfristiger Personalservice zur Seite</p>
    </div>

    <div class="block" style="top:466px">
      <h3>Der zuverlässige Empfangsdienst und Hostessenservice</h3>
      <p>Unser Personal wird vor jedem Auftrag detailliert eingearbeitet. Dafür machen wir uns vorab ein genaues Bild der Gegebenheiten, planen alle Aufgaben und Aufgabenbereiche und teilen sie den Mitarbeitern und Mitarbeiterinnen zu. So können Sie sich darauf verlassen, dass der Empfang und die Betreuung Ihrer Gäste und Kunden zu Ihrer vollsten Zufriedenheit umgesetzt werden. Wir informieren Sie regelmäßig über den Stand der Dinge: Sie haben den Überblick, genießen einen hervorragenden Empfangsdienst oder Hostessenservice und können sich in Ruhe um andere Aufgaben kümmern.</p>
    </div>

    <div class="block" style="top:553px">
      <h3>Sicherheit liegt uns am Herzen</h3>
      <p>Als Experte im Bereich Personenschutz und Sicherheitsdienstleistungen kennt sich die KWT SECURA GmbH bestens in allen Sicherheitsbelangen aus. Sie benötigen einen Empfangsdienst mit Kenntnissen im Bereich Sicherheit? Kein Problem für uns: Wir haben die entsprechend ausgebildete Fachkräfte, auf die Sie sich auch im Ernstfall absolut verlassen können. Sprechen Sie uns an!</p>
    </div>

    <div class="reasons">
      <h4>Vier gute Gründe für den Empfangsservice von KWT SECURA:</h4>
      <ul>
        <li><svg width="9" height="8" viewBox="0 0 9 8"><path d="M1 4.5 L3.3 7 L8 1" fill="none" stroke="#1d1d1f" stroke-width="1.3"/></svg>Höfliche und zuvorkommende<br>Begrüßung von Gästen und Besuchern</li>
        <li><svg width="9" height="8" viewBox="0 0 9 8"><path d="M1 4.5 L3.3 7 L8 1" fill="none" stroke="#1d1d1f" stroke-width="1.3"/></svg>Hervorragend ausgebildete Fachkräfte</li>
        <li><svg width="9" height="8" viewBox="0 0 9 8"><path d="M1 4.5 L3.3 7 L8 1" fill="none" stroke="#1d1d1f" stroke-width="1.3"/></svg>Sicherer Auftritt und ein gepflegtes Äußeres</li>
        <li><svg width="9" height="8" viewBox="0 0 9 8"><path d="M1 4.5 L3.3 7 L8 1" fill="none" stroke="#1d1d1f" stroke-width="1.3"/></svg>Auf Kundenwunsch Mitarbeiter mit zusätzlichen Fremdsprachen- und EDV-Kenntnissen</li>
      </ul>
    </div>
  </section>

  <section class="page-right">
    <div class="photo-shop" role="img" aria-label="Foto: Kundin betrachtet Kleidung an einer Kleiderstange im Geschäft"></div>
    <div class="page-no">13</div>
    <div class="tag-dark">KWT SECURA</div>
    <h2 class="title-right">SICHERHEIT IM <b>EINZELHANDEL</b></h2>
    <p class="intro-right">Dreiste Kunden, Ladendiebe oder Vandalen: Viele Einzelhändler kennen sie nur zu gut. Ladendiebstahl stellt ein ernst zu nehmendes Problem dar und sorgt langfristig für Umsatzeinbußen. Das muss nicht sein! Mit dem zuverlässigen Service der KWT SECURA GmbH sorgen Sie endlich für Sicherheit im Einzelhandel – professionell und wirkungsvoll!</p>

    <div class="col c1">
      <p><span class="sub">KWT SECURA – Sicherheit im Einzelhandel</span><br>Dreiste Kunden, Ladendiebe oder Vandalen: Viele Einzelhändler kennen sie nur zu gut. Ladendiebstahl stellt ein ernst zu nehmendes Problem dar und sorgt langfristig für Umsatzeinbußen. Das muss nicht sein! Mit dem zuverlässigen Service der KWT SECURA GmbH sorgen Sie endlich für Sicherheit im Einzelhandel – professionell und wirkungsvoll!</p>
      <p><span class="sub">Keine Chance für Ladendiebe und Vandalen</span><br>Als Experte für Einzelhandel-Sicherheit und Objektschutz berät Sie die KWT SECURA GmbH umfassend. Wir führen sämtliche Sicherheitsaufgaben in Geschäften durch. Ob Sie über einen kleinen Laden oder eine Handelskette mit mehreren großflächigen Verkaufsflächen verfügen, die KWT SECURA schützt Ihr Objekt zuverlässig. Gerne beraten wir Sie über Ihre Möglichkeiten, denn im Bereich Sicherheit für den Einzelhandel haben Sie viele Optionen: Wir setzen für Sie Kaufhaus-Detektive ein, platzieren Wachpersonal an allen kritischen Stellen und übernehmen die Bestreifung der Auf unseren Service können Sie sich hundertprozentig verlassen, sodass Sie sich in aller Ruhe auf Ihr Tagesgeschäft konzentrieren können.</p>
      <p><span class="sub">Sicherheit im Einzelhandel: Der Top-Service durch professionelle Mitarbeiter</span><br>Wir von der KWT SECURA GmbH legen höchsten Wert auf Zuverlässigkeit. Deswegen arbeiten für Ihre Sicherheit im Einzelhandel sorgfältig</p>
    </div>

    <div class="col c2">
      <p>ausgewählte Mitarbeiter. Das Security-Team der KWT SECURA besteht aus bestens geschulten Profis, die genau wissen, was sie tun und wie sie sich zu verhalten haben. Selbst randalierende Personen oder andere kritische Vorfälle stellen kein Problem dar. Unsere Mitarbeiter behalten in jeder Situation die nötige Ruhe und Professionalität. Zudem arbeitet unser gesamtes Team strikt nach § 34a der deutschen Gewerbeordnung und erhält regelmäßig relevante Weiterbildungen. Dazu gehören Auffrischungskurse sowie Zusatz- und Sonderlehrgänge. So können Sie sicher sein, dass in Ihrem Geschäft zu jeder Zeit optimal ausgebildetes Sicherheitspersonal arbeitet.</p>
      <p><span class="sub">Flexible und individuelle Sicherheitsleistungen</span><br>Von uns erhalten Sie keine x-beliebige Sicherheitslösung. Denn wir schreiben die persönliche Beratung und Betreuung unserer Kunden groß. Unsere Sicherheitsexperten machen sich vor Ort ein umfassendes Bild und erstellen ein genau auf Ihr Objekt zugeschnittenes Konzept. Anstatt einer x-beliebigen Lösung erhalten Sie individuellen Schutz und Sicherheit im Einzelhandel unter der Berücksichtigung aller spezifischen Schwachpunkte und Risikofaktoren. Ein Sicherheitskonzept von uns hält auch im Ernstfall das, was es verspricht. Das können wir Ihnen durch unsere langjährige Erfahrung und unzählige erfolgreiche</p>
    </div>

    <div class="col c3">
      <p>Praxiseinsätze garantieren. Über die aktuelle Sicherheitslage werden Sie natürlich regelmäßig informiert: Unsere Objektleiter senden regelmäßig Tages- und Nachtjournale an Ihre verantwortlichen Mitarbeiter im Management.</p>
      <p><span class="sub">Sicherheit und mehr: Das umfassende Leistungsspektrum der KWT SECURA</span><br>Wir bieten Ihnen nicht nur umfassende Sicherheit durch unsere Mitarbeiter vor Ort. Bei uns können Sie noch von vielen weiteren praktischen Services profitieren. An Informationspunkten setzen wir auf Wunsch beispielsweise Hostessen ein, die mit einem besonders freundlichen Auftreten und exzellenten Umgangsformen überzeugen. Gerne unterstützt Sie die KWT SECURA GMBH auch mit weiteren Sonderdienstleistungen wie Geld- und Werttransporten, dem Gutschein-Vertrieb oder der Eventabsicherung.</p>
      <p><span class="sub">Buchen Sie jetzt unverbindlich Ihren Erstberatungstermin</span><br>Die KWT SECURA sorgt auch in Ihrem Betrieb für Sicherheit im Einzelhandel. Vereinbaren Sie jetzt unverbindlich Ihren persönlichen Beratungstermin und wir klären Sie über Ihre Möglichkeiten auf. So erhalten Sie einen umfassenden Überblick über unsere Leistungen. Melden Sie sich noch heute per Telefon unter der Nummer 0800 555 0142 oder per E-Mail. Als Sicherheitsexperten sind wir gerne für Sie da!</p>
    </div>
  </section>

</div>
</body>
</html>
```